Design for online reviews widget

Attached is a wireframe of a widget we need designing to display reviews on websites from multiple sources. We need this provided at 3 different sizes including full screen, contained (like the wireframe) and mobile.
You have completely free rein on the styling.
The only elements that should remain untouched are the blue stars (https://www.filquarry.net/s/8vtmwp2291zq4h/kv%20stars.ai?dl=0) and powered by logo at the bottom.
Ignore the menu at the top of the wireframe, this is just from the website the widget will be placed on.
Businesses

```html
<!DOCTYPE html>
<html lang="en">
<head>
<meta charset="utf-8">
<title>Review Widget – Screen Sizes</title>
<link href="https://fonts.googleapis.com/css2?family=Poppins:wght@400;500;600;700&display=swap" rel="stylesheet">
<style>
:root{
  --stage:#a5a5a5;
  --panel:#ffffff;
  --card:#eaf7fc;
  --accent:#2cb7ea;
  --ink:#1b1b1b;
  --muted:#333;
  --gold:#f0bd3a;
  --time:#7a3fe0;
  --tick:#3cb449;
  --line:#2cb7ea;
}
*{box-sizing:border-box;margin:0;padding:0}
html,body{width:843px;height:1200px;overflow:hidden}
body{background:var(--stage);font-family:'Poppins',sans-serif;color:var(--ink);position:relative}
.screen-title{position:absolute;font-weight:600;text-align:center;letter-spacing:.2px;color:#111}
.panel{position:absolute;background:var(--panel)}
.score-stars{position:absolute;left:0;right:0;display:flex;justify-content:center}
.score-caption{position:absolute;left:0;right:0;text-align:center;font-weight:500}
.card{position:absolute;background:var(--card)}
.source-box{position:absolute;background:#fff;border-radius:5px;box-shadow:0 1px 4px rgba(0,0,0,.08);display:flex;flex-direction:column;align-items:center;justify-content:center;gap:4px}
.source-box.outlined{border:1px solid var(--accent)}
.source-name{font-weight:600;color:var(--ink)}
.source-score{font-weight:700;color:var(--accent)}
.rating{display:flex}
.review{position:absolute}
.review h3{font-weight:500;color:var(--ink)}
.review p{color:var(--muted)}
.hl{color:var(--accent);font-weight:600}
.metrics{display:flex;flex-wrap:wrap}
.metrics span{border-right:1.5px solid var(--line)}
.metrics span:last-child{border-right:none}
.meta{display:flex;align-items:center;font-weight:500}
.meta svg{flex:none}
.meta-row{display:flex;justify-content:space-between}
.load-more{position:absolute;background:var(--accent);color:#fff;border-radius:3px;font-weight:600;display:flex;align-items:center;justify-content:center}
.powered{position:absolute;text-align:right}
.powered small{display:block;font-weight:500}
.powered .brand{display:flex;align-items:center;gap:4px;font-weight:700;color:var(--ink)}
.powered .dot{border-radius:50%;background:var(--accent)}

/* wide layouts */
.wide .score-stars{top:11px;gap:8px}
.wide .score-stars svg{width:24px;height:24px}
.wide .score-caption{font-size:6.5px;top:40px}
.wide .source-box{width:97px;height:78px}
.wide .source-name{font-size:12px}
.wide .source-score{font-size:9px}
.wide .rating svg{width:13px;height:13px}
.wide .review h3{font-size:11.5px;line-height:1.2;margin-bottom:2px}
.wide .review p{font-size:6.4px;line-height:11px}
.wide .metrics{font-size:8px;margin-top:7px}
.wide .metrics span{padding:0 4px}
.wide .metrics span:first-child{padding-left:0}
.wide .meta{font-size:8px;gap:8px;margin-top:8px}
.wide .meta svg{width:9px;height:9px}
.wide .load-more{width:83px;height:25px;font-size:8px;top:520px;left:250px}
.wide .powered{top:515px;right:20px}
.wide .powered small{font-size:7.5px}
.wide .powered .brand{font-size:12px}
.wide .powered .dot{width:12px;height:12px}
.contained .review p{line-height:8.5px}
.contained .load-more{top:521px}
.contained .powered{top:516px;right:62px}

/* mobile */
.mobile .score-stars{top:26px;gap:8px}
.mobile .score-stars svg{width:23px;height:23px}
.mobile .score-caption{top:51px;font-size:9.3px}
.mobile .source-box{left:22px;top:12px;width:160px;height:46px;flex-direction:row;gap:10px}
.mobile .source-name{font-size:11px}
.mobile .source-score{font-size:9px}
.mobile .rating svg{width:12px;height:12px}
.mobile .review{left:14px;right:12px}
.mobile .review h3{font-size:8.4px;line-height:12.5px;margin-bottom:4px}
.mobile .review p{font-size:6px;line-height:9px}
.mobile .metrics{font-size:6.6px;margin-top:10px;row-gap:4px}
.mobile .metrics span{padding:0 4px}
.mobile .metrics span:first-child,.mobile .metrics span:last-child{padding-left:0}
.mobile .metrics span:nth-child(3){border-right:none}
.mobile .meta{font-size:9px;gap:10px;margin-top:10px}
.mobile .meta.small{font-size:7px;gap:8px}
.mobile .meta svg{width:10px;height:10px}
.mobile .load-more{left:62px;top:1058px;width:90px;height:27px;font-size:8.5px}
.mobile .powered{right:5px;top:1101px}
.mobile .powered small{font-size:5px}
.mobile .powered .brand{font-size:9px}
.mobile .powered .dot{width:10px;height:10px}
</style>
</head>
<body>
<svg width="0" height="0" style="position:absolute" aria-hidden="true">
  <defs>
    <symbol id="blue-star" viewBox="0 0 48 48">
      <circle cx="24" cy="24" r="23" fill="#2cb7ea"/>
      <circle cx="24" cy="24" r="17" fill="none" stroke="#fff" stroke-width="2.5"/>
      <path d="M24 12l3.5 7.3 8 1.1-5.8 5.6 1.4 8L24 30.2 16.9 34l1.4-8-5.8-5.6 8-1.1z" fill="#fff"/>
    </symbol>
    <symbol id="gold-star" viewBox="0 0 24 24">
      <path d="M12 1.5l3.2 6.6 7.3 1-5.3 5.1 1.3 7.2L12 18l-6.5 3.4 1.3-7.2L1.5 9.1l7.3-1z" fill="#f0bd3a"/>
    </symbol>
    <symbol id="tick" viewBox="0 0 16 16">
      <rect x="1" y="2" width="13" height="13" rx="1.5" fill="#3cb449"/>
      <path d="M4 8.5l3 3 7-8" fill="none" stroke="#fff" stroke-width="2"/>
    </symbol>
    <symbol id="pin" viewBox="0 0 16 16">
      <rect x="1" y="1" width="14" height="14" rx="2" fill="#3cb449"/>
      <path d="M4 8l3 3 5-6" fill="none" stroke="#fff" stroke-width="2"/>
    </symbol>
    <symbol id="hourglass" viewBox="0 0 16 16">
      <path d="M3 1h10M3 15h10M4 1c0 4 4 5 4 7s-4 3-4 7M12 1c0 4-4 5-4 7s4 3 4 7" fill="none" stroke="#7a3fe0" stroke-width="2"/>
    </symbol>
  </defs>
</svg>

<!-- FULL SCREEN -->
<div class="screen-title" style="left:13px;width:583px;top:4px;font-size:17px">FULL SCREEN</div>
<section class="panel wide full" style="left:13px;top:33px;width:583px;height:556px">
  <div class="score-stars">
    <svg><use href="#blue-star"/></svg><svg><use href="#blue-star"/></svg><svg><use href="#blue-star"/></svg><svg><use href="#blue-star"/></svg><svg><use href="#blue-star"/></svg>
  </div>
  <div class="score-caption">Combined Review Score 4.3 out of 5</div>

  <article class="card" style="left:0;right:0;top:59px;height:114px">
    <div class="source-box" style="left:24px;top:18px"><span class="source-name">HomeGrader</span><span class="source-score">9.77</span></div>
    <div class="review" style="left:145px;right:26px;top:10px">
      <h3>Front door with windows each side and side window</h3>
      <p>This is the second time we have used Paragon home Imp rovments , and the service is amazing! Declan came round several times as we keep changing our minds and he was so helpful and gave us good advice, and the guys who do the fitting are efficient and tidy . I've got to say the end result is amazing and I have recommended to many of friends .<br>Thanks Paragon</p>
      <div class="metrics"><span>Reliablity : <b class="hl">9.38</b></span><span>Courtesy : <b class="hl">10</b></span><span>Tidiness : <b class="hl">9.84</b></span><span>Workmanship : <b class="hl">10</b></span></div>
      <div class="meta-row">
        <div class="meta"><svg><use href="#tick"/></svg><span>Verified <span class="hl">28th September 2021</span></span></div>
        <div class="meta"><svg><use href="#pin"/></svg><span>Located in <span class="hl">Oakfield</span></span></div>
      </div>
    </div>
  </article>

  <article class="card" style="left:0;right:0;top:181px;height:111px">
    <div class="source-box outlined" style="left:24px;top:17px"><span class="source-name">Findora</span><div class="rating"><svg><use href="#gold-star"/></svg><svg><use href="#gold-star"/></svg><svg><use href="#gold-star"/></svg><svg><use href="#gold-star"/></svg><svg><use href="#gold-star"/></svg></div></div>
    <div class="review" style="left:145px;right:26px;top:10px">
      <h3>Positive: Professionalism, Quality, Value</h3>
      <p>The team did a good job of replacing a large feature window spanning two floors, as well as the others in my property. They're a professional group who were willing to work out solutions to any problem, especially compared to other companies. Prices are fair, and my new UPVC windows look great. Special thanks to Ron for being so accommodating and for the good communication throughout.</p>
      <div class="metrics"><span>Service : <b class="hl">Window installation</b></span></div>
      <div class="meta"><svg><use href="#hourglass"/></svg><span>11 months ago by <span class="hl">Peter Hale</span></span></div>
    </div>
  </article>

  <article class="card" style="left:0;right:0;top:300px;height:104px">
    <div class="source-box" style="left:24px;top:13px"><span class="source-name">Dirwell</span><div class="rating"><svg><use href="#gold-star"/></svg><svg><use href="#gold-star"/></svg><svg><use href="#gold-star"/></svg><svg><use href="#gold-star"/></svg><svg><use href="#gold-star"/></svg></div></div>
    <div class="review" style="left:145px;right:26px;top:9px">
      <h3>Brilliant all round professional, friendly service</h3>
      <p>This home run friendly business was a real pleasure to deal with. From the professional, no pressure quote, nothing was too much trouble to ensure everything is as required for your needs with the quote and fitting. The workmanship and double glazing being fitted was brilliant and my home/outdoors was left tidy and clean leaving an outstanding impression for such an all round professional job. I would not hesitate to recommend this company, such a brilliant service from great hardworking people that care about their service</p>
      <div class="meta"><svg><use href="#hourglass"/></svg><span>13 Feb 2018 by <span class="hl">GreenChair42</span></span></div>
    </div>
  </article>

  <article class="card" style="left:0;right:0;top:412px;height:94px">
    <div class="source-box outlined" style="left:24px;top:8px"><span class="source-name">Vouchly</span><div class="rating"><svg><use href="#gold-star"/></svg><svg><use href="#gold-star"/></svg><svg><use href="#gold-star"/></svg><svg><use href="#gold-star"/></svg><svg><use href="#gold-star"/></svg></div></div>
    <div class="review" style="left:145px;right:26px;top:9px">
      <h3>Front door with windows each side and side window</h3>
      <p>This is the second time we have used Paragon home Improvments , and the service is amazing! Declan came round several times as we keep changing our minds and he was so helpful and gave us good advice, and the guys who do the fitting are efficient and tidy . I've got to say the end result is amazing and I have recommended to many of friends . Thanks Paragon</p>
      <div class="meta"><svg><use href="#hourglass"/></svg><span>13 Feb 2018 by <span class="hl">Jo</span></span></div>
    </div>
  </article>

  <div class="load-more">Load More</div>
  <div class="powered"><small>Powered by</small><div class="brand"><span class="dot"></span>ReviewPool</div></div>
</section>

<!-- CONTAINED SCREEN -->
<div class="screen-title" style="left:13px;width:583px;top:595px;font-size:12px">CONTAINED SCREEN</div>
<section class="panel wide contained" style="left:13px;top:614px;width:583px;height:557px">
  <div class="score-stars">
    <svg><use href="#blue-star"/></svg><svg><use href="#blue-star"/></svg><svg><use href="#blue-star"/></svg><svg><use href="#blue-star"/></svg><svg><use href="#blue-star"/></svg>
  </div>
  <div class="score-caption">Combined Review Score 4.3 out of 5</div>

  <article class="card" style="left:62px;width:459px;top:60px;height:114px;border-radius:4px">
    <div class="source-box" style="left:11px;top:18px"><span class="source-name">HomeGrader</span><span class="source-score">9.77</span></div>
    <div class="review" style="left:120px;right:9px;top:9px">
      <h3>Front door with windows each side and side window</h3>
      <p>This is the second time we have used Paragon home Imp rovments , and the service is amazing! Declan came round several times as we keep changing our minds and he was so helpful and gave us good advice, and the guys who do the fitting are<br>efficient and tidy . I've got to say the end result is amazing and I have recommended to many of friends . Thanks Paragon</p>
      <div class="metrics"><span>Reliablity : <b class="hl">9.38</b></span><span>Courtesy : <b class="hl">10</b></span><span>Tidiness : <b class="hl">9.84</b></span><span>Workmanship : <b class="hl">10</b></span></div>
      <div class="meta-row">
        <div class="meta"><svg><use href="#tick"/></svg><span>Verified <span class="hl">28th September 2021</span></span></div>
        <div class="meta"><svg><use href="#pin"/></svg><span>Located in <span class="hl">Oakfield</span></span></div>
      </div>
    </div>
  </article>

  <article class="card" style="left:62px;width:459px;top:182px;height:111px;border-radius:4px">
    <div class="source-box" style="left:11px;top:17px"><span class="source-name">Findora</span><div class="rating"><svg><use href="#gold-star"/></svg><svg><use href="#gold-star"/></svg><svg><use href="#gold-star"/></svg><svg><use href="#gold-star"/></svg><svg><use href="#gold-star"/></svg></div></div>
    <div class="review" style="left:120px;right:9px;top:9px">
      <h3>Positive: Professionalism, Quality, Value</h3>
      <p>The team did a good job of replacing a large feature window spanning two floors, as well as the others in my property. They're a professional group who were willing to work out solutions to any problem, especially compared to other companies. Prices are fair, and my new UPVC windows look great. Special thanks to Ron for being so accommodating and for the good communication throughout.</p>
      <div class="metrics"><span>Service : <b class="hl">Window installation</b></span></div>
      <div class="meta"><svg><use href="#hourglass"/></svg><span>11 months ago by <span class="hl">Peter Hale</span></span></div>
    </div>
  </article>

  <article class="card" style="left:62px;width:459px;top:301px;height:106px;border-radius:4px">
    <div class="source-box" style="left:11px;top:14px"><span class="source-name">Dirwell</span><div class="rating"><svg><use href="#gold-star"/></svg><svg><use href="#gold-star"/></svg><svg><use href="#gold-star"/></svg><svg><use href="#gold-star"/></svg><svg><use href="#gold-star"/></svg></div></div>
    <div class="review" style="left:120px;right:9px;top:9px">
      <h3 style="margin-bottom:6px">Brilliant all round professional, friendly service</h3>
      <p>This home run friendly business was a real pleasure to deal with. From the professional, no pressure quote, nothing was too much trouble to ensure everything is as required for your needs with the quote and fitting. The workmanship and double glazing being fitted was brilliant and my home/outdoors was left tidy and clean leaving an outstanding impression for such an all round professional job. I would not hesitate to recommend this company, such a brilliant service from great hardworking people that care about their service</p>
      <div class="meta"><svg><use href="#hourglass"/></svg><span>13 Feb 2018 by <span class="hl">GreenChair42</span></span></div>
    </div>
  </article>

  <article class="card" style="left:62px;width:459px;top:415px;height:97px;border-radius:4px">
    <div class="source-box" style="left:11px;top:9px"><span class="source-name">Vouchly</span><div class="rating"><svg><use href="#gold-star"/></svg><svg><use href="#gold-star"/></svg><svg><use href="#gold-star"/></svg><svg><use href="#gold-star"/></svg><svg><use href="#gold-star"/></svg></div></div>
    <div class="review" style="left:120px;right:9px;top:9px">
      <h3 style="margin-bottom:4px">Front door with windows each side and side window</h3>
      <p>This is the second time we have used Paragon home Improvments , and the service is amazing! Declan came round several times as we keep changing our minds and he was so helpful and gave us good advice, and the guys who do the fitting are<br>efficient and tidy . I've got to say the end result is amazing and I have recommended to many of friends . Thanks Paragon</p>
      <div class="meta"><svg><use href="#hourglass"/></svg><span>13 Feb 2018 by <span class="hl">Jo</span></span></div>
    </div>
  </article>

  <div class="load-more">Load More</div>
  <div class="powered"><small>Powered by</small><div class="brand"><span class="dot"></span>ReviewPool</div></div>
</section>

<!-- MOBILE SCREEN -->
<div class="screen-title" style="left:607px;width:214px;top:4px;font-size:17px">MOBILE SCREEN</div>
<section class="panel mobile" style="left:607px;top:33px;width:214px;height:1133px">
  <div class="score-stars">
    <svg><use href="#blue-star"/></svg><svg><use href="#blue-star"/></svg><svg><use href="#blue-star"/></svg><svg><use href="#blue-star"/></svg><svg><use href="#blue-star"/></svg>
  </div>
  <div class="score-caption">Combined Review Score 4.3 out of 5</div>

  <article class="card" style="left:5px;width:204px;top:81px;height:266px;border-radius:4px">
    <div class="source-box"><span class="source-name">HomeGrader</span><span class="source-score">9.77</span></div>
    <div class="review" style="top:71px">
      <h3>Front door with windows each side and side window</h3>
      <p>This is the second time we have used Paragon home Imp rovments , and the service is amazing! Declan came round several times as we keep changing our minds and he was so helpful and gave us good advice, and the guys who do the fitting are<br>efficient and tidy . I've got to say the end result is amazing and I have recommended to many of friends .<br>Thanks Paragon</p>
      <div class="metrics"><span>Reliablity : <b class="hl">9.38</b></span><span>Courtesy : <b class="hl">10</b></span><span>Tidiness : <b class="hl">9.84</b></span><span>Workmanship : <b class="hl">10</b></span></div>
      <div class="meta"><svg><use href="#pin"/></svg><span>Located in <span class="hl">Oakfield</span></span></div>
      <div class="meta"><svg><use href="#tick"/></svg><span>Verified <span class="hl">28th September 2021</span></span></div>
    </div>
  </article>

  <article class="card" style="left:5px;width:204px;top:360px;height:217px;border-radius:4px">
    <div class="source-box"><span class="source-name">Findora</span><div class="rating"><svg><use href="#gold-star"/></svg><svg><use href="#gold-star"/></svg><svg><use href="#gold-star"/></svg><svg><use href="#gold-star"/></svg><svg><use href="#gold-star"/></svg></div></div>
    <div class="review" style="top:70px">
      <h3>Positive: Professionalism, Quality, Value</h3>
      <p>The team did a good job of replacing a large feature window spanning two floors, as well as the others in my property. They're a professional group who were willing to work out solutions to any problem, especially compared to other companies. Prices are fair, and my new UPVC windows look great. Special thanks to Ron for being so accommodating and for the good communication throughout.</p>
      <div class="metrics"><span>Service : <b class="hl">Window installation</b></span></div>
      <div class="meta small"><svg><use href="#hourglass"/></svg><span>11 months ago by <span class="hl">Peter Hale</span></span></div>
    </div>
  </article>

  <article class="card" style="left:5px;width:204px;top:590px;height:226px;border-radius:4px">
    <div class="source-box"><span class="source-name">Dirwell</span><div class="rating"><svg><use href="#gold-star"/></svg><svg><use href="#gold-star"/></svg><svg><use href="#gold-star"/></svg><svg><use href="#gold-star"/></svg><svg><use href="#gold-star"/></svg></div></div>
    <div class="review" style="top:70px">
      <h3>Brilliant all round professional, friendly service</h3>
      <p>This home run friendly business was a real pleasure to deal with. From the professional, no pressure quote, nothing was too much trouble to ensure everything is as required for your needs with the quote and fitting. The workmanship and double glazing being fitted was brilliant and my home/outdoors was left tidy and clean leaving an outstanding impression for such an all round professional job. I would not hesitate to recommend this company, such a brilliant service from great hardworking people that care about their service</p>
      <div class="meta small"><svg><use href="#hourglass"/></svg><span>13 Feb 2018 by <span class="hl">GreenChair42</span></span></div>
    </div>
  </article>

  <article class="card" style="left:5px;width:204px;top:834px;height:208px;border-radius:4px">
    <div class="source-box"><span class="source-name">Vouchly</span><div class="rating"><svg><use href="#gold-star"/></svg><svg><use href="#gold-star"/></svg><svg><use href="#gold-star"/></svg><svg><use href="#gold-star"/></svg><svg><use href="#gold-star"/></svg></div></div>
    <div class="review" style="top:70px">
      <h3>Front door with windows each side and side window</h3>
      <p>This is the second time we have used Paragon home Improvments , and the service is amazing! Declan came round several times as we keep changing our minds and he was so helpful and gave us good advice, and the guys who do the fitting are<br>efficient and tidy . I've got to say the end result is amazing and I have recommended to many of friends .<br>Thanks Paragon</p>
      <div class="meta small"><svg><use href="#hourglass"/></svg><span>13 Feb 2018 by <span class="hl">Jo</span></span></div>
    </div>
  </article>

  <div class="load-more">Load More</div>
  <div class="powered"><small>Powered by</small><div class="brand"><span class="dot"></span>ReviewPool</div></div>
</section>
</body>
</html>
```